Brightmoor Fire Solutions business card, logo and web design.

We need business cards for our new company. We are based in South Africa. We specialise in fire detection, fire prevention, security, access control and CCTV in buildings. We service and install sprinkler systems, fire hose reals and fire extinguishers in buildings. Our slogan in the company is "Compliance is our business" . We strive to be innovators in our field and deliver the best service possible at the best quality. We want to be the best in our field. We don't have any colour preferences as long as it relates to our type of business.
Our target market is clients that owns big buildings with multiple levels, such a malls,office buildings or warehouses.

Target Market(s)

Industry/Entity Type

Fire Safety

Contact Information for Business Card

The front of the card should have the company name (Brightmoor Fire Solutions (PTY) LTD. and a description of the company. Fire engineering & security services.

Logo Text

Compliance is our business

Number of Pages Required

4 page

Font styles to use
Serif

Colors

Designer to choose colors to be used in the design.

Requirements
Must have
• The company name, the logo and all the details on the back of the card. It should be simple and not to busy.
Nice to have
• Just something different and new. Brightmoor means - innovate so the card should represent our name.
Should not have
• Small pictures or lots of graphics on.

```html
<!DOCTYPE html>
<html lang="en">
<head>
<meta charset="utf-8">
<title>Brightmoor Fire Solutions – Business Card</title>
<link href="https://fonts.googleapis.com/css2?family=Open+Sans:ital,wght@0,400;0,600;1,400&display=swap" rel="stylesheet">
<style>
  :root{
    --stage:#2a2a2a;
    --card-dark:#282828;
    --card-light-a:#dcdcdc;
    --card-light-b:#c4c4c4;
    --flame:#e8552c;
    --ink:#1e1e1e;
    --ink-soft:#3a3a3a;
    --mist:#9a9a9a;
  }
  *{box-sizing:border-box;margin:0;padding:0}
  html,body{width:1200px;height:716px;overflow:hidden;background:var(--stage)}
  .canvas{position:relative;width:1200px;height:716px;font-family:"Open Sans",sans-serif}

  .card{position:absolute;width:500px;height:286px;border-radius:16px;box-shadow:0 10px 30px rgba(0,0,0,.45)}
  .card-front{left:60px;top:60px;background:var(--card-dark);display:flex;flex-direction:column;align-items:center;justify-content:center;text-align:center}
  .card-back{left:640px;top:290px;background:linear-gradient(135deg,var(--card-light-a),var(--card-light-b))}

  /* company name set plainly in the card's text face */
  .company{display:flex;align-items:center;gap:10px;font-family:"Open Sans",sans-serif;font-weight:600;color:var(--flame);line-height:1.2}
  .company-square{flex:none;background:var(--flame)}

  .card-front .company{font-size:24px}
  .card-front .company-square{width:14px;height:14px}
  .descriptor{font-style:italic;color:var(--flame);text-transform:uppercase;letter-spacing:.04em}
  .card-front .descriptor{font-size:11px;margin-top:14px}
  .slogan{font-size:13px;color:var(--mist);letter-spacing:.12em;text-transform:uppercase;margin-top:8px}

  .holder{position:absolute;left:26px;top:24px;padding-left:20px}
  .holder::before{content:"";position:absolute;left:0;top:2px;width:8px;height:40px;background:var(--flame)}
  .holder-name{font-size:19px;font-weight:600;color:var(--ink);text-transform:uppercase;letter-spacing:.02em}
  .holder-role{font-size:12px;color:var(--flame);text-transform:uppercase}

  .contact-list{position:absolute;left:26px;top:134px;list-style:none}
  .contact-list li{display:flex;align-items:center;gap:9px;font-size:13px;color:var(--ink-soft);height:21px}
  .contact-list svg{width:12px;height:12px;fill:var(--flame);flex:none}

  .card-back .brand{position:absolute;right:26px;top:92px;display:flex;flex-direction:column;align-items:flex-end}
  .card-back .company{font-size:13px}
  .card-back .company-square{width:9px;height:9px}
  .card-back .descriptor{font-size:8px;margin-top:4px}

  .website{position:absolute;right:26px;bottom:20px;font-size:13px;color:var(--flame)}

  .lockup{position:absolute;left:46px;top:600px}
  .lockup .company{font-size:32px}
  .lockup .company-square{width:20px;height:20px}
  .lockup .descriptor{font-size:14px;margin-top:12px;letter-spacing:.06em}
</style>
</head>
<body>
<main class="canvas">
  <section class="card card-front">
    <div class="company"><span class="company-square"></span>Brightmoor Fire Solutions (PTY) LTD</div>
    <p class="descriptor">Fire Engineering &amp; Security Services</p>
    <p class="slogan">Compliance is our business</p>
  </section>

  <section class="card card-back">
    <div class="holder">
      <h1 class="holder-name">Johan Marais</h1>
      <p class="holder-role">BSc(QS)(UP) . Managing Director</p>
    </div>
    <ul class="contact-list">
      <li><svg viewBox="0 0 24 24"><path d="M6.6 10.8a15 15 0 0 0 6.6 6.6l2.2-2.2a1 1 0 0 1 1-.25 11.4 11.4 0 0 0 3.6.57 1 1 0 0 1 1 1V20a1 1 0 0 1-1 1A17 17 0 0 1 3 4a1 1 0 0 1 1-1h3.5a1 1 0 0 1 1 1c0 1.25.2 2.45.57 3.6a1 1 0 0 1-.25 1z"/></svg>+27 (0)12 555 0142</li>
      <li><svg viewBox="0 0 24 24"><path d="M6 3h10v5H6zM3 9h18v9h-3v3H6v-3H3zm5 6v4h8v-4z"/></svg>+27 (0)12 555 0187</li>
      <li><svg viewBox="0 0 24 24"><path d="M7 1h10a2 2 0 0 1 2 2v18a2 2 0 0 1-2 2H7a2 2 0 0 1-2-2V3a2 2 0 0 1 2-2zm0 3v14h10V4z"/></svg>+27 (0)83 555 0163</li>
      <li><svg viewBox="0 0 24 24"><path d="M2 5h20v14H2zm2 2v.5l8 5 8-5V7z"/></svg>johan@brightmoorfire.co.za</li>
      <li><svg viewBox="0 0 24 24"><path d="M12 2a7 7 0 0 1 7 7c0 5-7 13-7 13S5 14 5 9a7 7 0 0 1 7-7zm0 4.5A2.5 2.5 0 1 0 12 11.5 2.5 2.5 0 0 0 12 6.5z"/></svg>12 Protea Street. Lynnwood. Pretoria. 0081</li>
    </ul>
    <div class="brand">
      <div class="company"><span class="company-square"></span>Brightmoor Fire Solutions (PTY) LTD</div>
      <p class="descriptor">Fire Engineering &amp; Security Services</p>
    </div>
    <p class="website">www.brightmoorfire.co.za</p>
  </section>

  <section class="lockup">
    <div class="company"><span class="company-square"></span>Brightmoor Fire Solutions (PTY) LTD</div>
    <p class="descriptor">Fire Engineering &amp; Security Services</p>
  </section>
</main>
</body>
</html>
```